TEK Logistics - Banner 2.5' x 8' for 20+ locations

Need a banner designed that will pop. This banner will be displayed at over 20 of our transportation facilities. Goal is for the banner to grab the attention of employees, contractors and clients and help reinforce our mission and core values. Designed needs to include TEK Logo, our core values and mission statement. Red and Black are the main company colors and we need to stay within that theme and color pallet. Attached is a previous version that was too basic and boring. Willing to consider a design that excludes the mission statement.

Gathering more feedback

```html
<!DOCTYPE html>
<html lang="en">
<head>
<meta charset="utf-8">
<title>TEK Logistics – Core Values Banner Options</title>
<link rel="stylesheet" href="https://fonts.googleapis.com/css2?family=Exo:wght@700&family=Fira+Sans+Condensed:ital,wght@1,400&display=swap">
<style>
  :root {
    --brand-red: #d2231a;
    --charcoal: #3a3a3a;
    --charcoal-light: #4a4845;
    --charcoal-dark: #333333;
    --ink: #2a2a2a;
    --white: #ffffff;
    --page: #ffffff;
  }
  html, body {
    margin: 0;
    padding: 0;
    width: 1200px;
    height: 900px;
    overflow: hidden;
    background: var(--page);
  }
  .canvas {
    position: relative;
    width: 1200px;
    height: 900px;
  }
  .banner {
    position: absolute;
    left: 176px;
    width: 878px;
    height: 275px;
    filter: drop-shadow(0 2px 4px rgba(0,0,0,0.35));
  }
  .banner--with-mission { top: 132px; }
  .banner--values-only { top: 467px; }
  .value {
    font-family: "Exo", "Arial Black", sans-serif;
    font-weight: 700;
  }
  .value--light { fill: var(--white); }
  .value--red { fill: var(--brand-red); }
  .mission {
    font-family: "Fira Sans Condensed", "Arial Narrow", sans-serif;
    font-style: italic;
    font-weight: 400;
    fill: var(--white);
  }
  .wordmark {
    font-family: "Exo", "Arial Black", sans-serif;
    font-weight: 700;
    fill: var(--ink);
  }
  .band-light { fill: url(#bandLight); }
  .band-dark { fill: var(--charcoal-dark); }
</style>
</head>
<body>
<main class="canvas">

  <!-- Option A: values plus mission statement -->
  <svg class="banner banner--with-mission" viewBox="0 0 1610 504" xmlns="http://www.w3.org/2000/svg" aria-label="TEK Logistics core values banner with mission statement">
    <defs>
      <linearGradient id="bandLight" x1="0" x2="1" y1="0" y2="0">
        <stop offset="0" stop-color="#55524e"/>
        <stop offset="0.5" stop-color="#3f3e3c"/>
        <stop offset="1" stop-color="#454441"/>
      </linearGradient>
    </defs>
    <rect class="band-dark" x="0" y="0" width="1610" height="504"/>
    <rect class="band-light" x="0" y="0" width="1610" height="80"/>
    <rect class="band-dark" x="0" y="80" width="1610" height="78"/>
    <rect class="band-light" x="0" y="158" width="1610" height="80"/>
    <rect class="band-dark" x="0" y="238" width="1610" height="78"/>
    <rect class="band-light" x="0" y="316" width="1610" height="80"/>

    <path fill="var(--white)" d="M0 0 H692 C600 60 540 130 490 200 L0 220 Z"/>
    <polygon fill="var(--brand-red)" points="390,396 1610,396 1610,504 272,504"/>
    <circle cx="200" cy="170" r="292" fill="var(--brand-red)"/>
    <circle cx="188" cy="165" r="275" fill="var(--white)"/>

    <text class="wordmark" x="200" y="220" font-size="96" text-anchor="middle">TEK</text>
    <text class="wordmark" x="200" y="268" font-size="36" text-anchor="middle" letter-spacing="8">LOGISTICS</text>

    <text class="value value--light" x="710" y="57" font-size="34" textLength="867" lengthAdjust="spacingAndGlyphs">DO THE RIGHT THINGS FOR THE RIGHT REASONS</text>
    <text class="value value--red" x="653" y="131" font-size="34" textLength="687" lengthAdjust="spacingAndGlyphs">PURSUE GROWTH AND DEVELOPMENT</text>
    <text class="value value--light" x="892" y="208" font-size="34" textLength="673" lengthAdjust="spacingAndGlyphs">BUILD A POSITIVE TEAM ATMOSPHERE</text>
    <text class="value value--red" x="560" y="285" font-size="34" textLength="610" lengthAdjust="spacingAndGlyphs">DELIVER WOW THROUGH SERVICE</text>
    <text class="value value--light" x="623" y="369" font-size="34" textLength="434" lengthAdjust="spacingAndGlyphs">DO EVERYTHING SAFELY</text>
    <text class="value value--red" x="1352" y="369" font-size="34" textLength="181" lengthAdjust="spacingAndGlyphs">HAVE FUN</text>

    <text class="mission" x="405" y="442" font-size="38" textLength="1152" lengthAdjust="spacingAndGlyphs">Provide the best customer experience while creating an environment of growth and</text>
    <text class="mission" x="532" y="480" font-size="38" textLength="895" lengthAdjust="spacingAndGlyphs">opportunity for our customers, employees, and service providers.</text>
  </svg>

  <!-- Option B: values only -->
  <svg class="banner banner--values-only" viewBox="0 0 1610 504" xmlns="http://www.w3.org/2000/svg" aria-label="TEK Logistics core values banner">
    <rect class="band-dark" x="0" y="0" width="1610" height="504"/>
    <rect class="band-light" x="0" y="0" width="1610" height="100"/>
    <rect class="band-dark" x="0" y="100" width="1610" height="100"/>
    <rect class="band-light" x="0" y="200" width="1610" height="102"/>
    <rect class="band-dark" x="0" y="302" width="1610" height="100"/>
    <rect class="band-light" x="0" y="402" width="1610" height="102"/>

    <path fill="var(--white)" d="M0 0 H692 C610 60 560 120 515 180 L0 220 Z"/>
    <circle cx="225" cy="185" r="294" fill="var(--brand-red)"/>
    <circle cx="208" cy="180" r="272" fill="var(--white)"/>

    <text class="wordmark" x="210" y="232" font-size="96" text-anchor="middle">TEK</text>
    <text class="wordmark" x="210" y="280" font-size="36" text-anchor="middle" letter-spacing="8">LOGISTICS</text>

    <text class="value value--light" x="687" y="69" font-size="40" textLength="903" lengthAdjust="spacingAndGlyphs">DO THE RIGHT THINGS FOR THE RIGHT REASONS</text>
    <text class="value value--red" x="588" y="166" font-size="40" textLength="789" lengthAdjust="spacingAndGlyphs">PURSUE GROWTH AND DEVELOPMENT</text>
    <text class="value value--light" x="793" y="266" font-size="40" textLength="794" lengthAdjust="spacingAndGlyphs">BUILD A POSITIVE TEAM ATMOSPHERE</text>
    <text class="value value--red" x="510" y="361" font-size="40" textLength="709" lengthAdjust="spacingAndGlyphs">DELIVER WOW THROUGH SERVICE</text>
    <text class="value value--light" x="542" y="466" font-size="40" textLength="505" lengthAdjust="spacingAndGlyphs">DO EVERYTHING SAFELY</text>
    <text class="value value--red" x="1339" y="466" font-size="40" textLength="226" lengthAdjust="spacingAndGlyphs">HAVE FUN</text>
  </svg>

</main>
</body>
</html>
```